Business card for a young aspring actress

My daughter is 18 and just starting out on her profession as an actress. She is a member of the Open Stage Company and has already had some extras work and a featured role in an upcoming Feature film.

She wants/needs a card that she can have to hand to give to those she comes into contact with in the theatre, TV and film industries.

We are thinking that it may be double sided with an impact side including a picture of her and her name etc with the reverse holding contact and other details.

She wants to go by the name Maren Joy Whitcombe.

She has done a little modelling but sees herself as an actress.

She can be seen in this video
http://www.hollybankacademy.example/videos/a3f19c7d5e2b8406c1d9e7f2a4b60835?width=640&height=480

Target Market(s)

Anyone she comes into contact with in theatre TV and film industries.

Industry/Entity Type

Business

Requirements
Nice to have
• She has email and a website www.marenwhitcombe.example She is quite a connected girl

```html
<!DOCTYPE html>
<html lang="en">
<head>
<meta charset="utf-8">
<title>Maren Joy Whitcombe – Actress business card</title>
<link rel="stylesheet" href="https://fonts.googleapis.com/css2?family=Arimo:ital,wght@0,400;0,700;1,400;1,700&display=swap">
<style>
  :root{
    --stage:#2a0f2e;
    --card-edge:#f07ab8;
    --magenta:#d8136a;
    --magenta-dark:#b80f5a;
    --magenta-deep:#c2105f;
    --hot:#ff1d6c;
    --blush:#f6b3df;
    --photo-light:#f7cfe3;
    --photo-mid:#eba3c8;
    --photo-deep:#c9608f;
    --ribbon:#f4eef2;
    --ribbon-text:#e0124f;
    --white:#ffffff;
    --slot:#5a1040;
  }
  *{box-sizing:border-box;margin:0;padding:0}
  html,body{width:1200px;height:900px;overflow:hidden}
  body{background:var(--stage);font-family:"Arimo",Arial,sans-serif;position:relative}

  .card{position:absolute;background:var(--card-edge);padding:10px;box-shadow:0 12px 30px rgba(0,0,0,.55)}
  .card__face{position:relative;width:100%;height:100%;background:var(--magenta);overflow:hidden}
  .card--front{left:70px;top:120px;width:550px;height:300px}
  .card--back{left:560px;top:500px;width:580px;height:290px}

  .panel{position:absolute;background:var(--magenta-dark)}
  .panel--light{background:var(--magenta-deep)}

  .photo{position:absolute;
    background:
      radial-gradient(ellipse 45% 35% at 50% 42%, var(--photo-light) 0%, rgba(247,207,227,0) 100%),
      linear-gradient(100deg, var(--photo-deep) 0%, var(--photo-mid) 30%, var(--photo-light) 55%, var(--photo-mid) 80%, var(--photo-deep) 100%)}
  .card--front .photo{right:0;top:0;width:180px;height:100%}
  .card--back .photo{left:205px;top:0;width:160px;height:100%;opacity:.9}

  .photo__caption{position:absolute;right:10px;bottom:8px;color:var(--white);font-size:10px;font-style:italic;letter-spacing:1px}

  .ribbon{position:absolute;width:260px;height:20px;background:var(--ribbon);color:var(--ribbon-text);
    font-size:11px;font-weight:700;text-align:center;line-height:20px;box-shadow:0 2px 4px rgba(0,0,0,.3)}
  .card--front .ribbon{left:-60px;top:48px;transform:rotate(-40deg)}
  .card--back .ribbon--left{left:-30px;top:26px;transform:rotate(-22deg)}
  .card--back .ribbon--right{right:-30px;top:26px;transform:rotate(22deg)}

  .name{position:absolute;background:var(--hot);color:var(--white);font-weight:700;font-size:21px;
    padding:6px 12px;box-shadow:3px 3px 5px rgba(0,0,0,.35);white-space:nowrap}
  .card--front .name{left:14px;top:112px}
  .card--back .name{left:170px;top:44px;background:rgba(255,80,140,.45);font-style:italic;font-size:18px;box-shadow:none;color:rgba(255,255,255,.85)}

  .role{position:absolute;background:var(--blush);color:var(--hot);font-weight:700;font-size:21px;
    padding:4px 24px;box-shadow:3px 3px 5px rgba(0,0,0,.3)}
  .card--front .role{left:104px;top:163px}
  .card--back .role{left:190px;top:152px;background:rgba(246,179,223,.9)}

  .links{position:absolute;display:flex;gap:6px;list-style:none}
  .card--front .links{left:16px;bottom:10px}
  .card--back .links{left:110px;bottom:12px}
  .link{width:46px;display:flex;flex-direction:column;align-items:center;gap:2px}
  .link__mark{width:36px;height:36px;background:var(--slot);border-radius:4px;display:flex;align-items:center;justify-content:center}
  .link__label{font-size:9px;font-weight:700;color:var(--white)}
  .link--web .link__mark{color:var(--white);font-size:10px;font-weight:700;text-align:center;line-height:11px}
</style>
</head>
<body>

<article class="card card--front">
  <div class="card__face">
    <div class="panel" style="left:0;top:0;width:120px;height:100%"></div>
    <div class="panel panel--light" style="left:120px;top:0;width:90px;height:100%"></div>
    <div class="photo" role="img" aria-label="Portrait photograph of the actress, pink toned">
      <span class="photo__caption">Maren Joy Whitcombe</span>
    </div>
    <div class="ribbon">www.marenwhitcombe.example</div>
    <h1 class="name">MAREN JOY WHITCOMBE</h1>
    <p class="role">ACTRESS</p>
    <ul class="links">
      <li class="link"><span class="link__mark"></span><span class="link__label">Vidora</span></li>
      <li class="link"><span class="link__mark"></span><span class="link__label">Circlo</span></li>
      <li class="link"><span class="link__mark"></span><span class="link__label">Murmur</span></li>
      <li class="link"><span class="link__mark"></span><span class="link__label">Callwave</span></li>
      <li class="link"><span class="link__mark"><svg width="26" height="18" viewBox="0 0 26 18"><rect x="1" y="1" width="24" height="16" fill="#eee" stroke="#999"/><path d="M1 1 L13 10 L25 1" fill="none" stroke="#999" stroke-width="1.5"/></svg></span><span class="link__label">Email</span></li>
      <li class="link link--web"><span class="link__mark">Web<br>Site</span><span class="link__label">&nbsp;</span></li>
    </ul>
  </div>
</article>

<article class="card card--back">
  <div class="card__face">
    <div class="panel" style="left:150px;top:0;width:280px;height:100%"></div>
    <div class="panel panel--light" style="left:0;top:250px;width:100%;height:40px"></div>
    <div class="photo" role="img" aria-label="Portrait photograph of the actress, pink toned"></div>
    <div class="ribbon ribbon--left">www.marenwhitcombe.example</div>
    <div class="ribbon ribbon--right">www.marenwhitcombe.example</div>
    <p class="name">MAREN JOY WHITCOMBE</p>
    <p class="role">ACTRESS</p>
    <ul class="links">
      <li class="link"><span class="link__mark"></span><span class="link__label">Vidora</span></li>
      <li class="link"><span class="link__mark"></span><span class="link__label">Circlo</span></li>
      <li class="link"><span class="link__mark"></span><span class="link__label">Murmur</span></li>
      <li class="link"><span class="link__mark"></span><span class="link__label">Callwave</span></li>
      <li class="link"><span class="link__mark"><svg width="26" height="18" viewBox="0 0 26 18"><rect x="1" y="1" width="24" height="16" fill="#eee" stroke="#999"/><path d="M1 1 L13 10 L25 1" fill="none" stroke="#999" stroke-width="1.5"/></svg></span><span class="link__label">Email</span></li>
      <li class="link link--web"><span class="link__mark">Web<br>Site</span><span class="link__label">&nbsp;</span></li>
    </ul>
  </div>
</article>

</body>
</html>
```